Copper Ridge Excursions Post Card/Flyer

Postcard/flyer needs to convey our mission: to provide an authentic, boutique wine tour of exceptional quality with first class customer service. It needs to be clean and high quality. Less is more :) Worthy of 5 star hotel concierges handing them to a guest. I provided an old flyer my friend made and my competitors flyer. Please use these just as reference, but i want to see your creativity. I like the format of "Meadow Harvest" -scan 91-flyer BUT I don't want to copy.
Updates

Need extra days to review

Target Market(s)

Couples, travelers, hotel employees, local industry, etc...

Industry/Entity Type

Boutique

Requirements
Must have
• Must have bullet points of the my previous reference flyer and any photos .Please use website for reference too.
• Revulo, route scout affirmations Plus Snapmora
• "Group and Private Tours available"
• "Mention this card for 10% off any tour" - low key please
• copperridgeexcursions.com, info@copperridgeexcursions.com, 805-618-2934
Nice to have
• clean lines , simple and elegant
• double sided please
Should not have
• Not too busy.

```html
<!DOCTYPE html>
<html lang="en">
<head>
<meta charset="utf-8">
<title>Copper Ridge Excursions – Flyer</title>
<link rel="stylesheet" href="https://fonts.googleapis.com/css2?family=Roboto:wght@500;700&family=Cormorant+Garamond:wght@500&display=swap">
<style>
  :root {
    --lime: #c4f06e;
    --lime-light: #d9f79a;
    --leaf: #6cb33f;
    --leaf-mid: #5aa335;
    --forest: #1f4d1e;
    --deep: #2e3b2a;
    --white: #ffffff;
    --band: #65ab3e;
    --badge: #6fae45;
    --brand: #3f5a2a;
  }
  * { margin: 0; padding: 0; box-sizing: border-box; }
  html, body { width: 1200px; height: 2432px; overflow: hidden; background: var(--white); }
  .flyer {
    position: relative;
    width: 1200px;
    height: 2432px;
    overflow: hidden;
    font-family: "Roboto", Arial, sans-serif;
    background: var(--white);
  }
  .hero-bg { position: absolute; left: 0; top: 0; width: 1200px; height: 1362px; }
  .features {
    position: absolute; left: 0; top: 0; width: 1200px;
    color: var(--forest); font-weight: 700; text-align: center;
    font-size: 41px; line-height: 46px;
  }
  .features p { position: absolute; left: 0; width: 1200px; }
  .photo { position: absolute; }
  .photo-pond { left: 32px; top: 1013px; width: 322px; height: 320px;
    background: linear-gradient(180deg, #3f7fd6 0%, #6fa7e8 35%, #6f8f3c 55%, #284f5e 75%, #5a7a35 100%); }
  .photo-patio { left: 388px; top: 1013px; width: 424px; height: 316px;
    background: linear-gradient(180deg, #a79a86 0%, #8b7a62 45%, #5f6b4a 75%, #7b6650 100%); }
  .photo-van { left: 850px; top: 1013px; width: 313px; height: 313px;
    background: linear-gradient(180deg, #2a63c4 0%, #7aa8e0 45%, #4e6a3a 65%, #3a3f3f 100%); }
  .reviews-band { position: absolute; left: 0; top: 1362px; width: 1200px; height: 260px; background: var(--white); }
  .review { position: absolute; top: 0; height: 260px; display: flex; align-items: center; justify-content: center; gap: 14px;
    color: var(--badge); font-weight: 700; font-size: 40px; }
  .review-snap { left: 150px; width: 270px; }
  .review-revulo { left: 455px; width: 270px; }
  .review-route { left: 750px; width: 300px; }
  .dot { width: 40px; height: 40px; border-radius: 50%; background: var(--badge); flex: none; }
  .square { width: 38px; height: 38px; background: var(--badge); flex: none; }
  .lime-strip { position: absolute; left: 0; top: 1622px; width: 1200px; height: 48px; background: var(--lime); }
  .contact {
    position: absolute; left: 0; top: 1670px; width: 1200px; height: 435px;
    background: var(--band); color: var(--white); text-align: center; font-weight: 700;
  }
  .contact p { position: absolute; left: 0; width: 1200px; }
  .contact .line { font-size: 55px; line-height: 60px; }
  .contact .offer { font-size: 31px; line-height: 36px; font-weight: 500; }
  .brand { position: absolute; left: 0; top: 2105px; width: 1200px; height: 327px; }
  .brand-bg { position: absolute; left: 0; top: 0; width: 1200px; height: 327px; }
  .brand-name {
    position: absolute; left: 0; top: 100px; width: 1200px; text-align: center;
    font-family: "Cormorant Garamond", Georgia, serif; font-weight: 500;
    font-size: 44px; letter-spacing: 3px; color: var(--brand);
  }
</style>
</head>
<body>
<main class="flyer">
  <svg class="hero-bg" viewBox="0 0 1200 1362" preserveAspectRatio="none" aria-hidden="true">
    <defs>
      <linearGradient id="heroFill" x1="0" y1="0" x2="1" y2="1">
        <stop offset="0" stop-color="#c9f27a"/>
        <stop offset="1" stop-color="#bde866"/>
      </linearGradient>
      <linearGradient id="leafSwoosh" x1="0" y1="0" x2="1" y2="0">
        <stop offset="0" stop-color="#b8e870"/>
        <stop offset="1" stop-color="#5aa335"/>
      </linearGradient>
    </defs>
    <rect width="1200" height="1362" fill="url(#heroFill)"/>
    <path d="M0 0 H1200 V60 C900 -10 500 60 0 180 Z" fill="url(#leafSwoosh)"/>
    <path d="M0 150 C400 60 800 20 1200 70 V110 C820 70 420 130 0 230 Z" fill="#ffffff" opacity="0.85"/>
    <path d="M700 170 C950 150 1120 200 1200 330 V140 C1100 120 900 130 700 170 Z" fill="#2f3d2c"/>
    <path d="M0 190 C420 100 820 90 1200 160 V260 C1120 180 900 160 600 200 C350 230 150 260 0 300 Z" fill="#c9f27a"/>
    <path d="M1150 200 C1200 260 1200 320 1200 340 V200 Z" fill="#6cb33f"/>
  </svg>

  <section class="features">
    <p style="top:260px">Come explore Santa Barbara<br>Wine Country with us!</p>
    <p style="top:396px">An Authentic and Boutique<br>Wine Tour Experience</p>
    <p style="top:534px">Premium wine tasting<br>at boutique wineries</p>
    <p style="top:671px">Safe and comfortable luxury vehicles</p>
    <p style="top:763px">Picnic lunch in a vineyard setting</p>
    <p style="top:854px">Local expert guides</p>
    <p style="top:945px">Group and private tours available</p>
  </section>

  <div class="photo photo-pond" role="img" aria-label="Vineyard pond with lily pads and an oak tree under a blue sky"></div>
  <div class="photo photo-patio" role="img" aria-label="Guests raising wine glasses on a stone winery patio"></div>
  <div class="photo photo-van" role="img" aria-label="Luxury tour van parked among vineyard hills"></div>

  <section class="reviews-band">
    <div class="review review-snap"><span class="square"></span>Snapmora</div>
    <div class="review review-revulo"><span class="dot"></span>Revulo</div>
    <div class="review review-route"><span class="dot"></span>route scout</div>
  </section>

  <div class="lime-strip"></div>

  <section class="contact">
    <p class="line" style="top:27px">Contact us for Availability</p>
    <p class="line" style="top:89px">info@copperridgeexcursions.com,</p>
    <p class="line" style="top:144px">805-618-2934</p>
    <p class="line" style="top:205px">copperridgeexcursions.com</p>
    <p class="offer" style="top:339px">"Mention this card for 10% off any tour"</p>
  </section>

  <footer class="brand">
    <svg class="brand-bg" viewBox="0 0 1200 327" preserveAspectRatio="none" aria-hidden="true">
      <rect width="1200" height="327" fill="#ffffff"/>
      <path d="M0 275 C400 240 800 250 1200 215 V327 H0 Z" fill="#c4f06e"/>
      <path d="M0 300 C450 265 850 280 1200 250 V327 H0 Z" fill="#6cb33f"/>
      <path d="M700 327 C900 300 1080 290 1200 275 V327 Z" fill="#2f3d2c"/>
    </svg>
    <p class="brand-name">COPPER RIDGE EXCURSIONS</p>
  </footer>
</main>
</body>
</html>
```